Pelton|Marsh & Quillan business card contest

We need a logo for an upscale boutique diversified company involved in real estate, investments, cattle, and more. Our businesses DO NOT need to be reflected in the business card nor do we want them noted. This is our logo and colors and we love our logo and colors. Our logo looks best against a black background and we like to include the firm name in our logo usage. importantly, the names Pelton and Marsh are separated by | not / and we use an ampersand not the word and.
On the front of the card, we want to include:
company logo and name (Pelton|Marsh & Quillan)
on the back, we would definitely include:
address, email, cell #
logo and name (smaller size than front)

The variable will be location of individual name and title (mine for example is ) - whether on the front OR on the back. interested in variations from which to choose
Dr. Neil R. Whitcombe, CFA
Scientifique des Fusées Financières

we would like to use contemporary symbols for address, email address, cell # with an option for web site that we do not intend to use initially. we like two sided cards and believe this design should use four rounded corners with the standard size. we prefer thicker card stock and may look at metal.

```html
<!DOCTYPE html>
<html lang="en">
<head>
<meta charset="utf-8">
<title>Pelton|Marsh &amp; Quillan — Business Card</title>
<link rel="stylesheet" href="https://fonts.googleapis.com/css2?family=Lato:wght@400;700&display=swap">
<style>
  :root {
    --stage: #e4e4e4;
    --card-dark: #0c0c0c;
    --card-light: #ffffff;
    --accent: #e4761c;
    --ink: #4a4a4a;
    --ink-soft: #8a8a8a;
    --rule: #d6d6d6;
  }
  * { box-sizing: border-box; margin: 0; padding: 0; }
  html, body {
    width: 1200px; height: 1015px; overflow: hidden;
    background: var(--stage);
    font-family: "Lato", sans-serif;
  }
  .stage {
    position: relative; width: 1200px; height: 1015px;
    display: flex; flex-direction: column; align-items: center; justify-content: center; gap: 44px;
  }
  .card {
    position: relative; width: 760px; height: 434px;
    border-radius: 14px; overflow: hidden;
    box-shadow: 0 10px 28px rgba(0,0,0,.18);
  }
  .card--front { background: var(--card-dark); }
  .card--back { background: var(--card-light); }

  .brand {
    position: absolute; display: flex; align-items: center; gap: 14px;
    font-weight: 400; color: var(--ink-soft); white-space: nowrap;
  }
  .brand__mark { background: var(--accent); flex: none; }
  .card--front .brand { left: 50%; top: 50%; transform: translate(-50%, -50%); font-size: 38px; }
  .card--front .brand__mark { width: 34px; height: 34px; }
  .card--back .brand { left: 48px; top: 196px; font-size: 25px; color: var(--ink); }
  .card--back .brand__mark { width: 24px; height: 24px; }

  .divider {
    position: absolute; left: 370px; top: 70px; width: 1px; height: 294px; background: var(--rule);
  }
  .details { position: absolute; left: 400px; top: 112px; color: var(--ink); }
  .details__name {
    font-weight: 700; font-size: 22px; color: var(--accent); text-transform: uppercase; letter-spacing: .2px;
  }
  .details__name span { font-weight: 400; }
  .details__title { font-size: 17px; margin-top: 2px; }
  .contact { list-style: none; margin-top: 14px; font-size: 17px; }
  .contact li { display: flex; align-items: center; gap: 9px; line-height: 27px; }
  .contact svg { width: 15px; height: 15px; flex: none; fill: var(--accent); }
  .address { margin-top: 8px; font-size: 17px; line-height: 24px; padding-left: 24px; }
</style>
</head>
<body>
<main class="stage">
  <section class="card card--front" aria-label="Card front">
    <div class="brand"><span class="brand__mark"></span>Pelton|Marsh &amp; Quillan</div>
  </section>

  <section class="card card--back" aria-label="Card back">
    <div class="brand"><span class="brand__mark"></span>Pelton|Marsh &amp; Quillan</div>
    <div class="divider"></div>
    <div class="details">
      <p class="details__name">Dr. Neil R. Whitcombe, <span>CFA</span></p>
      <p class="details__title">Scientifique des Fusées Financières</p>
      <ul class="contact">
        <li><svg viewBox="0 0 16 16" aria-hidden="true"><path d="M2 5c0-2 3-3 6-3s6 1 6 3v1h-3V5H5v1H2zM4 7h8l2 6H2zM8 8.5a1.8 1.8 0 1 0 0 3.6 1.8 1.8 0 0 0 0-3.6z"/></svg>044-210 387 654</li>
        <li><svg viewBox="0 0 16 16" aria-hidden="true"><path d="M1 3h14v10H1zM2.5 4.5 8 9l5.5-4.5v-.2H2.5z" fill-rule="evenodd"/></svg>info@pmqgroup.com</li>
        <li><svg viewBox="0 0 16 16" aria-hidden="true"><path d="M8 1a7 7 0 1 0 0 14A7 7 0 0 0 8 1zm0 2a5 5 0 0 1 4.6 3H9l-1 2 2 2-1 3H8A5 5 0 0 1 3.4 6H6z"/></svg>www.pmqgroup.com</li>
      </ul>
      <p class="address">18 Ashgrove Lane,<br>47310, Northmere</p>
    </div>
  </section>
</main>
</body>
</html>
```